Velmora Capital, a private equity fund, needs a brochure

Velmora Capital is a private equity fund dedicated to the development of budget hotels in France (reasonably priced hotel rooms).
Our customers are French private and high-income investors.

The brochure should communicate :
- seriousness and expertise
- trust, confidence and security
- financial product and profitability

The title is : Investissez dans l'hôtellerie économique et l'immobilier

Brochure size :
3 pages A4
Open size : 63 x 29,7 cm
Closed size : 21 x 29,7 cm

Our competitors :
Trelundo http://trelundo-immo-exemple.fr/
789 Horizon http://www.789horizon-exemple.com/
RWL Capital http://www.rwlgx-exemple.com/
Sorvel capital http://www.sorvelcapital-exemple.fr/
Darmetis http://www.darmeto-exemple.fr/

Target Market(s)

Private investors, high-income ; Institutional investors ; Target customers are French private investors with high revenue.

Industry/Entity Type

Financial

Requirements
Must have
• - Brochure must respect our identity (you can see our logo) and use its colors and typo (and/or same typo style)
- You must use pictures on each interior pages (pictures of projetc and hotels)

```html
<!DOCTYPE html>
<html lang="fr">
<head>
<meta charset="utf-8">
<title>Velmora Capital — Brochure</title>
<link href="https://fonts.googleapis.com/css2?family=Arimo:ital,wght@0,400;0,700;1,400;1,700&display=swap" rel="stylesheet">
<style>
:root{
  --backdrop:#a7a7a7;
  --paper:#ffffff;
  --brand-red:#9b1c23;
  --ink:#3a3a3a;
  --ink-soft:#555;
  --bullet:#c4c4c4;
  --rule-grey:#bdbdbd;
  --tag-grey:#8f8f8f;
  --blue-light:#4f81bd;
  --blue-mid:#2f5f96;
  --blue-dark:#1d3d68;
  --sky:#d6e4f2;
}
*{box-sizing:border-box;margin:0;padding:0}
html,body{width:1200px;height:900px;overflow:hidden;background:var(--backdrop);font-family:"Arimo",Arial,sans-serif;color:var(--ink)}
.spread{position:relative;width:1200px;height:900px}
.page{position:absolute;top:172px;width:390px;height:555px;background:var(--paper);overflow:hidden}
.page--one{left:15px}.page--two{left:408px}.page--three{left:800px;width:385px}
.page-spine{position:absolute;left:0;top:0;width:14px;height:100%;background:#eeeeee}
.page-spine::before{content:"";position:absolute;left:0;top:0;width:6px;height:120px;background:var(--brand-red)}
.spine-name{position:absolute;left:-1px;bottom:10px;width:14px;height:110px;}
.spine-name span{position:absolute;left:50%;top:50%;transform:translate(-50%,-50%) rotate(-90deg);white-space:nowrap;font-size:10px;letter-spacing:.5px;color:var(--brand-red);font-weight:400}
.page-body{position:absolute;left:32px;right:14px;top:28px}
h2{font-size:10px;font-weight:400;text-transform:uppercase;color:#444;line-height:1.1;margin:8px 0 3px}
h2 strong{color:var(--brand-red);font-weight:700}
h3.why{font-size:10px;font-style:italic;font-weight:700;color:var(--brand-red);text-transform:uppercase;margin:8px 0 3px}
p{font-size:5.6px;line-height:1.38;margin-bottom:3px;text-align:justify}
p.law{color:var(--brand-red);font-style:italic;font-weight:700}
ul.points{list-style:none;margin:3px 0 4px 18px}
ul.points li{position:relative;font-size:5.6px;line-height:1.35;padding-left:16px;margin-bottom:5px}
ul.points li::before{content:"";position:absolute;left:0;top:0;border-left:7px solid var(--bullet);border-top:4px solid transparent;border-bottom:4px solid transparent}
.quote{position:relative;display:flex;align-items:center;margin:6px 0 4px}
.quote-text{flex:1;padding:8px 28px 8px 20px;font-size:6.5px;text-transform:uppercase;text-align:center;line-height:1.6;color:var(--ink-soft)}
.quote-mark{position:absolute;color:var(--brand-red);font-size:26px;font-weight:700;line-height:1}
.portrait{width:48px;height:48px;background:linear-gradient(135deg,#9b9b9b,#5a5a5a);border:1px solid #ccc}
.split{display:flex;gap:10px}
.split p{flex:1.1}
.split ul{flex:1;margin:0}
.split ul li{margin-bottom:6px}
.slogan{position:relative;margin-top:14px;height:70px}
.slogan span{position:absolute;font-size:11px;font-style:italic;color:#666;text-transform:uppercase;letter-spacing:.3px}
.gain-chart{position:absolute;left:30px;top:8px}
.page-three-body{position:absolute;left:30px;right:14px;top:218px}
h2.split-title{font-size:10px;margin-top:10px}
.share-title{font-size:10px;text-transform:uppercase;color:#444;text-align:center;margin:20px 0 8px}
.share-row{display:flex;align-items:center;height:9px;margin-bottom:4px}
.share-tag{font-size:5.5px;text-transform:uppercase;letter-spacing:.6px;height:9px;line-height:9px;text-align:center}
.share-tag--class{width:65px;border:1px solid #bbb;color:#666}
.share-tag--role{width:65px;margin-left:5px;background:var(--tag-grey);color:#fff}
.share-bar{height:8px;background:var(--brand-red);margin-left:5px}
.share-value{font-size:12px;color:#555;margin-left:10px;letter-spacing:1px}
</style>
</head>
<body>
<div class="spread">

  <!-- Page 1 -->
  <section class="page page--one">
    <div class="page-spine"><div class="spine-name"><span>VELMORA CAPITAL</span></div></div>
    <div class="page-body">
      <h2>Un véhicule innovant</h2>
      <p>VELMORA CAPITAL (Hôtels Budget Choisis) est une société d'investissement constituée sous la forme d'une SAS à capital variable ayant opté pour le régime fiscal des sociétés de capital-risque (« SCR »).</p>
      <p class="law">Les Société de capital-risque bénéficient d'un régime fiscal de faveur prévu par la Loi n° 85-695 du 11 juillet 1985 et les dispositions légales et réglementaires du Code général des impôts.</p>
      <p>Les associés personnes physiques peuvent bénéficier d'un régime d'exonération d'impôt sur le revenu pour les dividendes perçus et les plus-values de cession de titres réalisées (seules les contributions sociales restant applicables) à condition notamment de conserver les actions et de réinvestir leurs produits dans la SCR pendant une durée de 5 ans. Les conditions d'application de ce régime sont présentées à titre indicatif et de manière synthétique dans un document annexe auquel il convient de se reporter.</p>

      <div class="quote">
        <span class="quote-mark" style="left:4px;top:-2px">“</span>
        <div class="quote-text">Nous nous positionnons sur des marchés en croissance<br>qui ont prouvé leur résistance face à la crise.</div>
        <span class="quote-mark" style="right:58px;bottom:-14px">”</span>
        <div class="portrait" role="img" aria-label="Portrait du dirigeant de la société"></div>
      </div>

      <h2>Une société de capital-risque conçue et gérée<br>par le <strong>Groupe Ardenta Outremer</strong></h2>
      <div class="split">
        <p>Fort d'une connaissance approfondie en ingénierie financière et en promotion immobilière, le Groupe Ardenta Outremer et ses filiales bénéficient d'une expérience de plus de vingt ans dans la structuration financière, juridique et fiscale d'investissements immobiliers et industriels.</p>
        <ul class="points">
          <li>4000 Projets structurés et financés depuis vingt ans.</li>
          <li>3000 Investisseurs satisfaits.</li>
          <li>800 Sociétés sous gestion.</li>
        </ul>
      </div>

      <h2>Des investissements centrés sur<br>l'hôtellerie et l'immobilier</h2>
      <p>VELMORA CAPITAL a pour objectif d'accueillir jusqu'à 30 millions d'euro de souscriptions sur 2 ans. Le produit de ces souscriptions permettra la prise de participations minoritaires (40% maximum) dans le capital de sociétés ayant pour objet :</p>
      <ul class="points">
        <li>La construction ou l'acquisition d'hôtels économiques et leur exploitation.</li>
        <li>La construction ou l'acquisition de meublés de tourisme et leur exploitation.</li>
        <li>La construction-vente d'immeuble en VEFA.</li>
      </ul>
      <p>L'activité d'VELMORA CAPITAL est notamment centrée sur l'investissement dans des sociétés développant une activité commerciale d'exploitation d'hôtels économiques. Ces sociétés du portefeuille seront à terme propriétaires des actifs immobiliers qu'elles exploitent.</p>
      <p>VELMORA CAPITAL pourra également diversifier ses investissements dans les secteurs de la promotion immobilière et de l'immobilier de service (meublés de tourisme et/ou résidences médicalisées).</p>

      <h3 class="why">Pourquoi l'hôtellerie et l'immobilier ?</h3>
      <p>Dans des conditions économiques et financières perturbées depuis la crise financière de 2008, les investisseurs exigent aujourd'hui des placements structurés pour résister aux effets économiques induits. Selon l'analyse des équipes de Velmora Capital, le marché de l'hôtellerie économique en croissance depuis sa création répond particulièrement bien à ces attentes. Ce positionnement est en adéquation avec la baisse des budgets alloués aux déplacements et voyages professionnels et touristiques.</p>
      <p>Le marché de l'immobilier reste quant à lui une valeur refuge en temps de crise, selon l'analyse des équipes de Velmora Capital</p>
      <ul class="points">
        <li>Un marché en croissance malgré la crise.</li>
        <li>Sur 2011, la croissance cumulée du nombre de nuitées atteint + 3,2% par rapport à 2010. (source Kestrel Data)</li>
        <li>Secteur porteur. 1,5 milliard d'euros ont été investis dans le secteur de l'hôtellerie en France en 2011 (source Kestrel Data)</li>
      </ul>
    </div>
  </section>

  <!-- Page 2 -->
  <section class="page page--two">
    <div class="page-spine"><div class="spine-name"><span>VELMORA CAPITAL</span></div></div>
    <div class="page-body">
      <h2>Un partenariat avec <strong>Lorvane Hotels Group</strong></h2>
      <p>Pour l'exploitation des investissements hôteliers, les sociétés du portefeuille interviendront en partenariat avec un opérateur hôtelier – LORVANE HOTELS GROUP – dans le cadre d'un accord de franchise (Lorvane Hotels Group, 2ème opérateur d'Europe, plus de 1000 hôtels dans le monde).</p>
      <ul class="points">
        <li>Contrats de franchise sous ses enseignes : Primavel **, Casteline *** et Iris Lodge ***.</li>
        <li>Contrats d'assistance technique.</li>
        <li>Implantation de plus de 12 hôtels dans 6 régions françaises d'outremer.</li>
      </ul>

      <h2>Focus sur l'hôtellerie économique dans les<br>régions françaises ultramarines</h2>
      <p>Le marché des hôtels économiques normés et standardisés sous enseigne nationale ou internationale est peu développé dans les DOM-COM. Ces régions sont équipées principalement d'hôtels balnéaires à vocation touristique essentiellement implantés sur des lieux généralement éloignés des centres économiques. Depuis une vingtaine d'années, le développement important des populations et la centralisation des zones commerciales et industrielles sur les capitales administratives ont généré d'importants embouteillages qui compliquent les accès à ces zones. L'offre hôtelière n'est plus en adéquation avec les attentes des visiteurs professionnels. La création d'une chaîne d'hôtels économiques est la réponse à ce besoin et bénéficie de l'appui de la puissance publique et des instances régionales.</p>
      <ul class="points">
        <li>Absence d'hôtels économiques standardisés et normés dans ces régions.</li>
        <li>Structures hôtelières existantes inadaptées aux besoins du marché professionnel et coûteuses : prix des nuitées proposées par ces nouveaux hôtels inférieurs de 30 à 50% aux prix pratiqués localement.</li>
        <li>Programmes d'investissements bénéficiant d'avantages fiscaux, sociaux et de subventions.</li>
      </ul>

      <h2>Immobilier, valeur refuge pour l'investisseur<br>(selon l'analyse d'Velmora Capital)</h2>
      <ul class="points">
        <li>Un investissement dans la pierre.</li>
        <li>Une réponse à l'incertitude des marchés financiers et de la monnaie et des risques d'inflation.</li>
        <li>Des emplacements exceptionnels (centres villes, aéroports, zones commerciales).</li>
      </ul>

      <h2>Trois sources potentielles de gains :</h2>
      <p>Une double plus-value potentielle hôtelière et immobilière assortie d'un rendement annuel. La création de valeur pour chacun des hôtels dans lesquels VELMORA CAPITAL prendra des participations proviendra de la valorisation des murs de l'hôtel, de la valorisation de son fonds de commerce et de la rentabilité annuelle de l'exploitation. L'activité de location de meublés de tourisme bénéficie des mêmes synergies.</p>
      <p>La création de valeur pour l'activité de promotion immobilière (construction vente des immeubles) proviendra des marges dégagées par les opérations de promotion</p>
      <ul class="points">
        <li>Trois sources potentielles de gains, assorties toutefois d'un risque de perte en capital</li>
        <li>Atténuation de risques du fait de l'investissement diversifié dans les murs et dans le fonds de commerce</li>
        <li>Un recours à un financement peu couteux</li>
      </ul>

      <div class="slogan">
        <span class="quote-mark" style="left:0;top:0">“</span>
        <span style="left:14px;top:14px">Plus-values hôtelières.</span>
        <span style="left:78px;top:34px">Plus-values immobilières.</span>
        <span style="left:18px;top:54px">Rendement annuel capitalisé.</span>
        <span class="quote-mark" style="left:270px;top:58px;color:var(--brand-red);font-style:normal">”</span>
      </div>
    </div>
  </section>

  <!-- Page 3 -->
  <section class="page page--three">
    <div class="page-spine"><div class="spine-name"><span>VELMORA CAPITAL</span></div></div>

    <svg class="gain-chart" width="345" height="205" viewBox="0 0 345 205" aria-label="Calendrier et composition des gains espérés">
      <defs>
        <linearGradient id="hopeFill" x1="0" y1="1" x2="1" y2="0">
          <stop offset="0" stop-color="#ffffff"/>
          <stop offset="1" stop-color="#b9cfe6"/>
        </linearGradient>
      </defs>
      <polygon points="10,115 215,18 215,115" fill="url(#hopeFill)"/>
      <line x1="10" y1="115" x2="210" y2="18" stroke="#c9878a" stroke-width="1.2"/>
      <polygon points="216,14 206,17 210,22" fill="#c9878a"/>
      <text x="160" y="82" font-size="8" fill="#1d3d68" text-anchor="middle" font-weight="700">Espérance de gains</text>
      <text x="160" y="93" font-size="8" fill="#1d3d68" text-anchor="middle" font-weight="700">pour l'investisseur</text>

      <rect x="215" y="17" width="98" height="35" fill="var(--blue-light)"/>
      <text x="264" y="37" font-size="6.2" fill="#fff" text-anchor="middle" font-weight="700">Plus values hôtelières</text>
      <rect x="215" y="54" width="98" height="28" fill="var(--blue-mid)"/>
      <text x="264" y="70" font-size="6.2" fill="#fff" text-anchor="middle" font-weight="700">Plus values immobilières</text>
      <rect x="215" y="84" width="98" height="31" fill="var(--blue-dark)"/>
      <text x="264" y="97" font-size="6.2" fill="#fff" text-anchor="middle" font-weight="700">Rendement annuel</text>
      <text x="264" y="106" font-size="6.2" fill="#fff" text-anchor="middle" font-weight="700">capitalisé</text>
      <rect x="316" y="17" width="16" height="98" fill="#fff" stroke="#8da9cc" stroke-width=".8"/>
      <text transform="translate(326,66) rotate(-90)" font-size="6" fill="#1d3d68" text-anchor="middle">Exonération fiscale</text>

      <rect x="10" y="122" width="120" height="30" fill="var(--brand-red)"/>
      <text x="40" y="140" font-size="6.2" fill="#fff" font-weight="700">Investissements</text>
      <line x1="130" y1="137" x2="218" y2="137" stroke="#ccc" stroke-width="1"/>
      <rect x="218" y="122" width="117" height="30" fill="var(--brand-red)"/>
      <text x="276" y="135" font-size="6.2" fill="#fff" text-anchor="middle" font-weight="700">Remboursement</text>
      <text x="276" y="144" font-size="6.2" fill="#fff" text-anchor="middle" font-weight="700">du capital initial</text>

      <g font-size="8" font-weight="700" fill="#333" text-anchor="middle">
        <rect x="12" y="162" width="28" height="15" fill="#d3d3d3"/><text x="26" y="173">2012</text>
        <rect x="45" y="162" width="28" height="15" fill="#d3d3d3"/><text x="59" y="173">2013</text>
        <rect x="78" y="162" width="28" height="15" fill="#d3d3d3"/><text x="92" y="173">2014</text>
        <rect x="138" y="162" width="28" height="15" fill="#d3d3d3"/><text x="152" y="173">2017</text>
        <rect x="207" y="162" width="28" height="15" fill="#d3d3d3"/><text x="221" y="173">2019</text>
      </g>
      <text x="152" y="186" font-size="6" fill="var(--brand-red)" font-weight="700" text-anchor="middle">Possibilité</text>
      <text x="152" y="194" font-size="6" fill="var(--brand-red)" font-weight="700" text-anchor="middle">de sortie</text>
    </svg>

    <div class="page-three-body">
      <p>L'attention des investisseurs est toutefois attirée sur l'impact de l'effet "moyenne" d'un tel affichage, lequel peut masquer de mauvais résultats pour certains fonds en particulier et lequel ne préjuge pas de performances d'un niveau équivalent pour le présent fond (étant en toutes hypothèses rappelé que Velmora Capital présente un risque de perte en capital). Par ailleurs, l'attention des investisseurs est attirée sur les facteurs de risques liés à un investissement dans Velmora Capital présentés ci-après dans le présent document</p>

      <h2 class="split-title">Comment sont répartis les gains ?</h2>
      <p>Le capital de la société VELMORA CAPITAL est constitué de deux types de catégorie d'actions A et B.</p>
      <ul class="points">
        <li>Les actions de type A destinées aux investisseurs.</li>
        <li>Les actions de type B (carried-interest) destinées à être souscrites par les personnes intervenant dans la gestion de VELMORA CAPITAL</li>
        <li>En vertu des dispositions légales et statutaires applicables, l'émission de 100 actions de type A oblige à émettre 1 action B Ne pouvant être souscrite que par les personnes intervenant dans la gestion de VELMORA CAPITAL.</li>
      </ul>
      <p>Les droits préférentiels attachés aux actions A et aux actions B sont définis à l'article 14.2 des statuts de Velmora Capital et répondent notamment au principe selon lequel l'actif net de liquidation au-delà d'un "rendement" de 7% l'an sera répartis à hauteur de 80% pour les actions A (investisseurs) et 20% pour les actions B (personnes intervenant dans la gestion du fonds).</p>

      <div class="share-title">Pertage des gains espérés</div>
      <div class="share-row">
        <span class="share-tag share-tag--class">Actions A</span>
        <span class="share-tag share-tag--role">Investisseur</span>
        <span class="share-bar" style="width:143px"></span>
        <span class="share-value">80 %</span>
      </div>
      <div class="share-row">
        <span class="share-tag share-tag--class">Actions B</span>
        <span class="share-tag share-tag--role">Gestionnaire</span>
        <span class="share-bar" style="width:36px"></span>
        <span class="share-value">20 %</span>
      </div>
    </div>
  </section>

</div>
</body>
</html>
```